Custom Die cut yard sign

Hi!

I would love to get really eye catching creative here with some window cleaning die cut signs!

I would like the main words to stand out of just saying, "Window Cleaning"

My phone number: 612-555-0148
Website: BrightpaneMN.com

My logo but it can be small as I want the "Window Cleaning and Phone number to really pop.

It can be a creative for implying window cleaning! Die cut so maybe water? Light? Windows outlines, squeegee? I don't know it's for residential window cleaning!

Attached is my logo and the template for the die cut sign.

Thanks!

```html
<!DOCTYPE html>
<html lang="en">
<head>
<meta charset="utf-8">
<title>Brightpane Window Cleaning – Yard Sign</title>
<link rel="stylesheet" href="https://fonts.googleapis.com/css2?family=Bebas+Neue&family=Montserrat:wght@600;700&display=swap">
<style>
  :root {
    --backdrop: #1c1c1d;
    --shadow: #000000;
    --navy: #16284f;
    --green: #8dc443;
    --sky-light: #c4e0ea;
    --sky-mid: #a7d1de;
    --sky-deep: #8fc3d4;
    --white: #ffffff;
  }
  html, body {
    margin: 0;
    padding: 0;
    width: 1200px;
    height: 943px;
    overflow: hidden;
    background: var(--backdrop);
  }
  .yard-sign {
    display: block;
    width: 1200px;
    height: 943px;
  }
  .headline {
    font-family: "Bebas Neue", "Oswald", sans-serif;
    fill: var(--navy);
  }
  .contact {
    font-family: "Montserrat", sans-serif;
  }
  .contact-phone {
    font-weight: 700;
    fill: var(--navy);
  }
  .contact-web {
    font-weight: 600;
    fill: var(--white);
  }
  .brand-name {
    font-family: "Montserrat", sans-serif;
    font-weight: 700;
    fill: var(--navy);
  }
  .brand-dot { fill: var(--navy); }
  .sign-shadow { fill: var(--shadow); }
  .swoosh-navy { fill: var(--navy); }
  .swoosh-green { fill: var(--green); }
</style>
</head>
<body>
<svg class="yard-sign" viewBox="0 0 1200 943" xmlns="http://www.w3.org/2000/svg">
  <defs>
    <linearGradient id="skyPhoto" x1="0" y1="0" x2="1" y2="1">
      <stop offset="0" stop-color="var(--sky-mid)"/>
      <stop offset="0.45" stop-color="var(--sky-light)"/>
      <stop offset="1" stop-color="var(--sky-deep)"/>
    </linearGradient>
    <clipPath id="signShape">
      <rect x="78" y="72" width="1028" height="771"/>
    </clipPath>
  </defs>

  <rect class="sign-shadow" x="86" y="80" width="1028" height="771"/>

  <g clip-path="url(#signShape)">
    <rect x="78" y="72" width="1028" height="771" fill="url(#skyPhoto)"
          role="img" aria-label="Photo of a blue window squeegee with a sponge edge lying on a light blue surface"/>

    <path class="swoosh-navy" d="M78,512 C250,600 480,625 700,590 C880,555 1030,420 1106,300 L1106,843 L78,843 Z"/>
    <path class="swoosh-green" d="M78,526 C250,620 420,665 620,655 C820,645 1000,560 1106,468 L1106,843 L78,843 Z"/>
  </g>

  <text class="headline" x="118" y="340" font-size="263" textLength="685" lengthAdjust="spacingAndGlyphs">WINDOW</text>
  <text class="headline" x="146" y="494" font-size="181" textLength="576" lengthAdjust="spacingAndGlyphs">CLEANING</text>

  <g class="brand">
    <circle class="brand-dot" cx="215" cy="568" r="34"/>
    <text class="brand-name" x="215" y="640" font-size="30" text-anchor="middle">Brightpane</text>
  </g>

  <text class="contact contact-phone" x="590" y="753" font-size="97" text-anchor="middle" textLength="615" lengthAdjust="spacingAndGlyphs">612-555-0148</text>
  <text class="contact contact-web" x="590" y="820" font-size="54" text-anchor="middle" textLength="697" lengthAdjust="spacingAndGlyphs">www.BrightpaneMN.com</text>
</svg>
</body>
</html>
```